BHSC Business cards

We are an established dental practice that is looking for new business cards to match our new logo. We are looking for something unique and sophisticated.
BRIEF: Colours are black, silver and white. Include the company name, logo (including “Pelwick Heath Dental Care”) and phone number “03 9415 2876”.
Front - Include the company name, logo (including “Pelwick Heath Dental Care”) and phone number “03 9415 2876”.
Back - Include the company name,  “Pelwick Heath Dental Care”, phone number “03 9415 2876”. address "64A Tindle Street, Pelwick Heath, Vic 3187", "Email reception@pelwickheathdentalcare.com.au", the Dentist Name " Dr ................................"  Your next appointment "Day, date and time(am/pm)".  3 lines for 3 appointments please, and at the bottom "IF UNABLE TO KEEP THIS APPOINTMENT 48 HOURS NOTICE IS REQUIRED."
Try and be creative and different with the design, i've added an image for inspiration

Target Market(s)
ALL in need of dental
Industry/Entity Type
Dental Clinic
Look and feel
Each slider illustrates characteristics of the customer's brand and the style your logo design should communicate.

```html
<!DOCTYPE html>
<html lang="en">
<head>
<meta charset="utf-8">
<title>Pelwick Heath Dental Care – Business Cards</title>
<link href="https://fonts.googleapis.com/css2?family=Poppins:wght@400;600;700&family=Roboto:wght@300;400&display=swap" rel="stylesheet">
<style>
  :root {
    --backdrop: #2b2a2a;
    --card-black: #1e1d1d;
    --card-white: #ffffff;
    --silver: #c9c9c9;
    --ink: #1a1a1a;
    --ink-soft: #444444;
  }
  * { box-sizing: border-box; margin: 0; padding: 0; }
  html, body {
    width: 1200px; height: 810px; overflow: hidden;
    background: var(--backdrop);
  }
  .canvas { position: relative; width: 1200px; height: 810px; }

  .card {
    position: absolute;
    width: 600px; height: 340px;
    box-shadow: 0 14px 30px rgba(0,0,0,.45);
  }
  .card--front { left: 70px; top: 70px; background: var(--card-black); }
  .card--back  { left: 530px; top: 410px; background: var(--card-white); color: var(--ink); }

  /* brand block */
  .brand { display: flex; align-items: center; gap: 14px; }
  .brand__dot { flex: none; border-radius: 50%; }
  .brand__text { display: flex; flex-direction: column; }
  .brand__name {
    font-family: "Poppins", sans-serif; font-weight: 600;
    text-transform: uppercase; line-height: 1.05;
  }
  .brand__phone {
    font-family: "Poppins", sans-serif; font-weight: 400;
    letter-spacing: .12em;
  }

  .card--front .brand {
    position: absolute; left: 90px; top: 128px;
  }
  .card--front .brand__dot { width: 74px; height: 74px; background: var(--silver); }
  .card--front .brand__name { color: var(--silver); font-size: 27px; letter-spacing: .04em; }
  .card--front .brand__phone { color: var(--silver); font-size: 15px; margin-top: 6px; }

  .card--back .brand { position: absolute; right: 34px; top: 28px; gap: 10px; }
  .card--back .brand__dot { width: 44px; height: 44px; background: var(--ink); }
  .card--back .brand__name { color: var(--ink); font-size: 16px; letter-spacing: .03em; }
  .card--back .brand__phone { color: var(--ink); font-size: 10px; margin-top: 3px; }

  /* appointment block */
  .appointment {
    position: absolute; left: 290px; top: 100px; width: 280px;
  }
  .appointment__title {
    font-family: "Poppins", sans-serif; font-weight: 700;
    font-size: 17px; letter-spacing: .02em; margin-bottom: 14px;
  }
  .appointment__line {
    display: flex; align-items: baseline;
    font-family: "Roboto", sans-serif; font-weight: 300;
    font-size: 13px; color: var(--ink-soft); margin-bottom: 14px;
  }
  .appointment__dots {
    flex: 1; border-bottom: 1.5px dotted #777; margin: 0 4px; height: 10px;
  }
  .appointment__dots--short { flex: 0 0 40px; }

  /* dentist contact */
  .dentist { position: absolute; left: 34px; top: 168px; }
  .dentist__name {
    font-family: "Poppins", sans-serif; font-weight: 700;
    font-size: 19px; letter-spacing: .02em; margin-bottom: 10px;
  }
  .dentist__detail {
    font-family: "Roboto", sans-serif; font-weight: 300;
    font-size: 12.5px; color: var(--ink-soft); line-height: 1.45;
  }
  .dentist__gap { height: 8px; }

  .notice {
    position: absolute; left: 34px; right: 30px; bottom: 20px;
    font-family: "Roboto", sans-serif; font-weight: 400;
    font-size: 12px; letter-spacing: .06em; text-transform: uppercase;
  }
</style>
</head>
<body>
<div class="canvas">

  <section class="card card--front" aria-label="Business card front">
    <div class="brand">
      <span class="brand__dot"></span>
      <div class="brand__text">
        <span class="brand__name">Pelwick Heath<br>Dental Care</span>
        <span class="brand__phone">03 9415 2876</span>
      </div>
    </div>
  </section>

  <section class="card card--back" aria-label="Business card back">
    <div class="brand">
      <span class="brand__dot"></span>
      <div class="brand__text">
        <span class="brand__name">Pelwick Heath Dental Care</span>
        <span class="brand__phone">03 9415 2876</span>
      </div>
    </div>

    <div class="appointment">
      <h2 class="appointment__title">NEXT APPOINTMENT</h2>
      <p class="appointment__line">Date <span class="appointment__dots"></span>At<span class="appointment__dots appointment__dots--short"></span>am/pm</p>
      <p class="appointment__line">Date <span class="appointment__dots"></span>At<span class="appointment__dots appointment__dots--short"></span>am/pm</p>
      <p class="appointment__line">Date <span class="appointment__dots"></span>At<span class="appointment__dots appointment__dots--short"></span>am/pm</p>
    </div>

    <div class="dentist">
      <h1 class="dentist__name">DR MARLEN OSKVIG</h1>
      <p class="dentist__detail">64A Tindle Street<br>Pelwick Heath, Vic 3187</p>
      <div class="dentist__gap"></div>
      <p class="dentist__detail">Phone: 03 9415 2876<br>E-mail: reception@pelwickheathdentalcare.com.au</p>
    </div>

    <p class="notice">If unable to keep this appointment please give 24 hours notice</p>
  </section>

</div>
</body>
</html>
```